Vehicles Brochure Diagram

Task Outline
Create diagrams for our new vehicles brochures

Task Description

Who are we:
KTW is New Zealand's largest Business Group Buying organisation, helping organisations nationwide reduce their running costs. We offer members the best deals from over 100 Contracted Suppliers, anything from vehicles, stationery to electronics and coffee.

The project:
We need 2 diagrams to illustrate the benefits of our vehicle services. The diagram will be used in our brochures (example attached)

1. A Diagram illustrating/explaining the elements that are involved in purchasing a new car & how our service ties it all together to provide the best solution.
- Please see the Diagram 1 PDF for a rough wireframe of the elements involved

2. Another small diagram inserted on an separate page to demonstrate how our services can increase safety & profit and reduce costs & risks (PDF: Diagram 2 Details)

The design needs to be clean, clear and simple that it’s easy to understand within a few seconds of looking at it. Feel free to explore with different elements in the realm of infographics, flowcharts & diagrams to best communicate the idea visually.
Updates

Just thought I’ll share some of the feedback we’re giving tosubmissions that have been coming through to help with new submissions

-Challenge & be creative about the ways you demonstratethe elements

-We don’t want to see your design replicating the ones that isdrawn. The purpose of it is only to provide you with the content in context

-We can’t emphasis enough that the style pdf is only areference and not the look you should imitate. 

If you have any question please feel free to contact me.Looking forward to see your designs!

Project Deadline Extended
Reason: We're keen to see more approaches & creative ways of interpreting the content rather than a standard cycle diagram. Entries so far have been good but quite literal, we will provide feedback to help steer it in the right direction.

Target Market(s)

Business professionals, Decision makers on a corporate level & prospects.

Industry/Entity Type

Electronics

Requirements
Must have

• Likes – simple, clean & clear, uncluttered

Dislikes – Overcrowded images, text, & colours. Overly expressive typeface. Please no literal illustration of our sketches or colored version of our sketch.

Font: -Myriad Pro

Colour: Please refer to the color palette in the ‘Diagram Color & Style’ PDF

The brochures are attached with content to provide context that might inform the design better,

Dimensions & the amount of space you have to work with will also be highlighted

```html
<!DOCTYPE html>
<html lang="en">
<head>
<meta charset="utf-8">
<title>Vehicle Purchase Cost Diagram</title>
<link rel="stylesheet" href="https://fonts.googleapis.com/css2?family=Source+Sans+3:wght@400;600;700&display=swap">
<style>
  :root {
    --navy: #134b8a;
    --heading: #1c4f8f;
    --item: #2a5fa6;
    --green: #5b9a41;
    --green-text: #5b9a41;
    --sky: #72b6e4;
    --sky-light: #bfe0f5;
    --price: #8cc8f0;
    --paper: #ffffff;
  }
  html, body {
    margin: 0;
    padding: 0;
    width: 1200px;
    height: 849px;
    overflow: hidden;
    background: var(--paper);
  }
  .diagram {
    display: block;
    width: 1200px;
    height: 849px;
    font-family: "Source Sans 3", sans-serif;
  }
  .title { fill: var(--navy); font-weight: 700; font-size: 44px; }
  .group-heading { fill: var(--heading); font-weight: 700; font-size: 33px; }
  .group-item { fill: var(--item); font-weight: 400; font-size: 25px; }
  .end-heading { fill: var(--green-text); font-weight: 700; font-size: 25px; }
  .end-item { fill: var(--green-text); font-weight: 400; font-size: 25px; }
  .price-label { fill: var(--price); font-weight: 700; font-size: 58px; letter-spacing: 1px; }
  .requirement-wedge, .manage-wedge { fill: var(--green); }
  .vehicle-area { fill: var(--navy); }
</style>
</head>
<body>
<svg class="diagram" viewBox="0 0 1200 849" xmlns="http://www.w3.org/2000/svg">
  <defs>
    <linearGradient id="road-fill" x1="0.85" y1="0" x2="0.1" y2="1">
      <stop offset="0" stop-color="var(--sky)"/>
      <stop offset="0.6" stop-color="var(--sky-light)"/>
      <stop offset="1" stop-color="#ffffff"/>
    </linearGradient>
    <linearGradient id="motion-fill" x1="0" y1="0" x2="1" y2="0.3">
      <stop offset="0" stop-color="var(--sky)"/>
      <stop offset="1" stop-color="#ffffff" stop-opacity="0"/>
    </linearGradient>
  </defs>

  <text class="title" x="600" y="60" text-anchor="middle">There is more to a vehicle purchase than just the</text>

  <polygon class="road" points="470,377 712,377 975,840 228,840" fill="url(#road-fill)"/>

  <polygon class="requirement-wedge" points="7,430 427,430 235,804"/>
  <polygon class="manage-wedge" points="754,430 1189,430 975,804"/>

  <path class="motion-trail" d="M811,278 C850,300 890,330 940,352 L940,363 C890,360 845,345 811,330 Z" fill="url(#motion-fill)"/>

  <g class="vehicle" role="img" aria-label="Flat front-view car icon in navy blue with a windscreen">
    <rect class="vehicle-area" x="384" y="88" width="427" height="336" rx="34"/>
    <text class="price-label" x="597" y="172" text-anchor="middle">PRICE</text>
  </g>

  <g class="end-of-life">
    <text class="end-heading" x="954" y="281" text-anchor="middle">End of Life</text>
    <text class="end-item" x="954" y="321" text-anchor="middle">Disposal Costs</text>
  </g>

  <g class="company-requirements" text-anchor="middle">
    <text class="group-heading" x="211" y="471">Your Company</text>
    <text class="group-heading" x="211" y="515">Requirements</text>
    <text class="group-item" x="220" y="554">Safety</text>
    <text class="group-item" x="224" y="597">Specifications</text>
    <text class="group-item" x="228" y="649">Sustainability</text>
  </g>

  <g class="cost-to-run" text-anchor="middle">
    <text class="group-heading" x="598" y="474">Cost to Run</text>
    <text class="group-item" x="598" y="516">Fuel</text>
    <text class="group-item" x="598" y="558">Tyres</text>
    <text class="group-item" x="598" y="601">Rego</text>
    <text class="group-item" x="598" y="644">RoC</text>
  </g>

  <g class="cost-to-manage" text-anchor="middle">
    <text class="group-heading" x="947" y="476">Cost to Manage</text>
    <text class="group-item" x="953" y="517">Lease</text>
    <text class="group-item" x="967" y="563">Finance &amp; Tax</text>
    <text class="group-item" x="967" y="608">Insurance</text>
  </g>
</svg>
</body>
</html>
```